Business Card Design Project

Beauty Therapist
Bold, bright, feminine, like contrast, love flowers, girly stuff. Must be beautiful. But open to all suggestions. Business name: Plush Clover.
xxx
Danuta Kaczmarczyk
Updates

Project Deadline Extended
Reason: I think you need more time to design something good. X

Target Market(s)

ignore this

Industry/Entity Type

Business

```html
<!DOCTYPE html>
<html lang="en">
<head>
<meta charset="utf-8">
<title>Plush Clover – Business Card</title>
<link rel="stylesheet" href="https://fonts.googleapis.com/css2?family=Raleway:wght@400;600;700&display=swap">
<style>
  :root {
    --bg: #e9e6e2;
    --card-black: #111112;
    --card-black-hi: #222225;
    --magenta: #ee1fa8;
    --magenta-deep: #c8108a;
    --text-light: #e8e8e8;
    --rule: #6b6b6b;
  }
  * { margin: 0; padding: 0; box-sizing: border-box; }
  html, body { width: 1200px; height: 1023px; overflow: hidden; }
  body {
    background: var(--bg);
    font-family: "Raleway", sans-serif;
    display: flex;
    flex-direction: column;
    align-items: center;
    justify-content: center;
    gap: 80px;
  }
  .card {
    position: relative;
    width: 700px;
    height: 400px;
    background: linear-gradient(150deg, var(--card-black-hi) 0%, var(--card-black) 60%);
    overflow: hidden;
    box-shadow: 0 10px 30px rgba(0,0,0,0.25);
  }
  .card .swoosh { position: absolute; inset: 0; width: 100%; height: 100%; }
  .brand {
    position: absolute;
    color: var(--magenta);
  }
  .brand-name {
    display: block;
    font-weight: 700;
    line-height: 1;
    white-space: nowrap;
  }
  .brand-tagline {
    display: block;
    color: var(--text-light);
    font-weight: 400;
    text-align: right;
    margin-top: 6px;
  }
  /* back side */
  .card-back .brand { left: 60px; top: 225px; }
  .card-back .brand-name { font-size: 40px; }
  .card-back .brand-tagline { font-size: 12px; }
  .contact {
    position: absolute;
    left: 300px;
    top: 70px;
    padding-left: 22px;
    border-left: 1px solid var(--rule);
    color: var(--text-light);
    font-size: 14px;
    line-height: 1.75;
  }
  .contact-name {
    color: var(--magenta);
    font-weight: 700;
    font-size: 16px;
    margin-bottom: 4px;
  }
  .contact-line { display: flex; align-items: center; gap: 10px; }
  .contact-line svg { width: 12px; height: 12px; fill: var(--text-light); flex: none; }
  /* front side */
  .card-front .brand { left: 140px; top: 150px; }
  .card-front .brand-name { font-size: 64px; }
  .card-front .brand-tagline { font-size: 15px; }
</style>
</head>
<body>

  <section class="card card-back" aria-label="Card back">
    <svg class="swoosh" viewBox="0 0 700 400" preserveAspectRatio="none" aria-hidden="true">
      <defs>
        <linearGradient id="swoosh-back" x1="0" y1="0" x2="1" y2="1">
          <stop offset="0" stop-color="var(--magenta)"/>
          <stop offset="1" stop-color="var(--magenta-deep)"/>
        </linearGradient>
      </defs>
      <path d="M700 0 L672 0 C640 70 610 120 560 170 C500 230 470 300 455 400 L700 400 Z" fill="url(#swoosh-back)"/>
    </svg>
    <div class="brand">
      <span class="brand-name">Plush Clover</span>
      <span class="brand-tagline">Beauty Therapist</span>
    </div>
    <div class="contact">
      <p class="contact-name">Danuta Kaczmarczyk</p>
      <p class="contact-line"><svg viewBox="0 0 24 24"><path d="M6.6 10.8a15 15 0 0 0 6.6 6.6l2.2-2.2a1 1 0 0 1 1-.25 11.4 11.4 0 0 0 3.6.57 1 1 0 0 1 1 1V20a1 1 0 0 1-1 1A17 17 0 0 1 3 4a1 1 0 0 1 1-1h3.5a1 1 0 0 1 1 1c0 1.25.2 2.45.57 3.57a1 1 0 0 1-.25 1z"/></svg>123.456.7890</p>
      <p class="contact-line"><svg viewBox="0 0 24 24"><path d="M2 5h20v14H2zm2 2v.5l8 5 8-5V7zm0 2.8V17h16V9.8l-8 5z"/></svg>xxxxxxxxxx@email.com</p>
      <p class="contact-line"><svg viewBox="0 0 24 24"><path d="M12 2a10 10 0 1 0 0 20 10 10 0 0 0 0-20zm0 2c.9 1.2 1.6 2.8 1.9 5h-3.8c.3-2.2 1-3.8 1.9-5zM4.3 13a8 8 0 0 1 0-2h3.8a18 18 0 0 0 0 2zm.8 2h3.2c.3 1.6.8 3 1.5 4a8 8 0 0 1-4.7-4zm3.2-6H5.1a8 8 0 0 1 4.7-4c-.7 1-1.2 2.4-1.5 4zM12 20c-.9-1.2-1.6-2.8-1.9-5h3.8c-.3 2.2-1 3.8-1.9 5zm2.1-7h-4.2a16 16 0 0 1 0-2h4.2a16 16 0 0 1 0 2zm.1 6c.7-1 1.2-2.4 1.5-4h3.2a8 8 0 0 1-4.7 4zm1.7-6a18 18 0 0 0 0-2h3.8a8 8 0 0 1 0 2zm-.2-4c-.3-1.6-.8-3-1.5-4a8 8 0 0 1 4.7 4z"/></svg>www.yourwebsite.com</p>
    </div>
  </section>

  <section class="card card-front" aria-label="Card front">
    <svg class="swoosh" viewBox="0 0 700 400" preserveAspectRatio="none" aria-hidden="true">
      <defs>
        <linearGradient id="swoosh-front" x1="0" y1="0" x2="1" y2="1">
          <stop offset="0" stop-color="var(--magenta)"/>
          <stop offset="1" stop-color="var(--magenta-deep)"/>
        </linearGradient>
      </defs>
      <path d="M700 0 L655 0 C640 60 610 120 565 175 C520 235 520 320 560 400 L700 400 Z" fill="url(#swoosh-front)"/>
    </svg>
    <div class="brand">
      <span class="brand-name">Plush Clover</span>
      <span class="brand-tagline">Beauty Therapist</span>
    </div>
  </section>

</body>
</html>
```